Tarvel Ridge LLC

Need Professional Business cards for New Investment Fund

Target Market(s)

High Quality investors

Industry/Entity Type

Financial

Contact Information for Business Card

Phone Number +1 555 284 6193
Name Pavel Orlinsky
Title Fund Manager
email po@FundTarvel.example
Website www.FundTarvel.example

Colors

Designer to choose colors to be used in the design.

Requirements
Must have
• Must have our Logo and all of the above. Must be made so lettering and loge can be raised

```html
<!DOCTYPE html>
<html lang="en">
<head>
<meta charset="utf-8">
<title>Tarvel Ridge LLC – Business Card</title>
<link href="https://fonts.googleapis.com/css2?family=Arimo:wght@400;700&display=swap" rel="stylesheet">
<style>
  :root {
    --page: #efefef;
    --ink-dark: #1c1c1c;
    --green-light: #4fa614;
    --green-deep: #178a1c;
    --brand-ink: #3a463c;
    --name-green: #22a51c;
    --accent-green: #1fc41a;
    --white: #ffffff;
  }
  html, body {
    margin: 0;
    width: 1200px;
    height: 1200px;
    overflow: hidden;
    background: var(--page);
    font-family: "Arimo", Arial, sans-serif;
  }
  .card {
    position: absolute;
    left: 235px;
    width: 730px;
    height: 417px;
    display: block;
  }
  .card--front { top: 131px; }
  .card--back { top: 652px; }
  .brand-name {
    font-family: "Arimo", Arial, sans-serif;
    font-weight: 700;
    fill: var(--brand-ink);
  }
  .holder-name {
    font-family: "Arimo", Arial, sans-serif;
    font-weight: 700;
    font-size: 32px;
    fill: var(--name-green);
  }
  .holder-title {
    font-family: "Arimo", Arial, sans-serif;
    font-weight: 400;
    font-size: 20px;
    fill: var(--white);
  }
  .contact-line {
    font-family: "Arimo", Arial, sans-serif;
    font-weight: 700;
    font-size: 16px;
    fill: var(--white);
  }
  .icon { fill: var(--white); }
</style>
</head>
<body>

<!-- Front of card -->
<svg class="card card--front" viewBox="0 0 730 417" xmlns="http://www.w3.org/2000/svg" aria-label="Business card front">
  <defs>
    <linearGradient id="paperFront" x1="0" y1="0" x2="1" y2="0">
      <stop offset="0" stop-color="#e6e6e6"/>
      <stop offset="1" stop-color="#fafafa"/>
    </linearGradient>
    <linearGradient id="artFront" x1="0" y1="0" x2="1" y2="1">
      <stop offset="0" stop-color="var(--green-deep)"/>
      <stop offset="1" stop-color="var(--green-light)"/>
    </linearGradient>
  </defs>
  <rect class="card-base" width="730" height="417" fill="var(--ink-dark)"/>
  <polygon class="card-paper" points="338,0 730,0 730,417 442,417 285,305" fill="url(#paperFront)"/>
  <polygon class="art-area" role="img" aria-label="Green folded-paper illustration"
           points="338,0 128,205 155,417 442,417 285,305" fill="url(#artFront)"/>

  <g class="brand">
    <rect x="433" y="196" width="22" height="22" fill="var(--accent-green)"/>
    <text class="brand-name" x="465" y="215" font-size="26">Tarvel Ridge</text>
  </g>
</svg>

<!-- Back of card -->
<svg class="card card--back" viewBox="0 0 730 417" xmlns="http://www.w3.org/2000/svg" aria-label="Business card back">
  <defs>
    <linearGradient id="paperBack" x1="0" y1="0" x2="1" y2="0">
      <stop offset="0" stop-color="#fafafa"/>
      <stop offset="1" stop-color="#e6e6e6"/>
    </linearGradient>
    <linearGradient id="artBack" x1="1" y1="0" x2="0" y2="1">
      <stop offset="0" stop-color="var(--green-deep)"/>
      <stop offset="1" stop-color="var(--green-light)"/>
    </linearGradient>
  </defs>
  <rect class="card-base" width="730" height="417" fill="var(--ink-dark)"/>
  <polygon class="card-paper" points="0,0 210,0 265,312 108,417 0,417" fill="url(#paperBack)"/>
  <polygon class="art-area" role="img" aria-label="Green folded-paper illustration"
           points="210,0 420,205 393,417 108,417 265,312" fill="url(#artBack)"/>

  <g class="brand">
    <rect x="50" y="196" width="20" height="20" fill="var(--accent-green)"/>
    <text class="brand-name" x="78" y="214" font-size="23">Tarvel Ridge</text>
  </g>

  <g class="holder">
    <text class="holder-name" x="530" y="81" text-anchor="middle">Pavel Orlinsky</text>
    <text class="holder-title" x="535" y="113" text-anchor="middle">Fund Manager</text>
    <rect class="rule" x="427" y="127" width="203" height="2" fill="var(--white)"/>
    <rect class="rule-accent" x="427" y="126" width="36" height="4" fill="var(--name-green)"/>
  </g>

  <g class="contacts">
    <path class="icon icon--phone" d="M437 300 l4 -1 l3 5 l-2 2 q2 4 6 6 l2 -2 l5 3 l-1 4 q-10 1 -17 -17z"/>
    <text class="contact-line" x="473" y="314">+1 555 284 6193</text>

    <g class="icon icon--mail">
      <rect x="435" y="330" width="16" height="11" fill="var(--white)"/>
      <path d="M435 330 l8 6 l8 -6" fill="none" stroke="var(--ink-dark)" stroke-width="1.4"/>
    </g>
    <text class="contact-line" x="469" y="339">po@FundTarvel.example</text>

    <path class="icon icon--pointer" d="M439 355 l0 16 l4 -4 l3 7 l2 -1 l-3 -7 l5 0z"/>
    <text class="contact-line" x="469" y="368">www.FundTarvel.example</text>
  </g>
</svg>

</body>
</html>
```